COMING SOON PAGE for BEAUTY WEBSITE

Looking for a very beautiful, high end coming soon page for the site, www.glowparlorqz.com

looking for the site to have a bit of text and fade thru a few images -- beautiful fonts, modern airy feel.

Text on page:

it doesn't have to be complicated
glowparlorqz.com coming soon
beauty, simplified.

Please use all lowercase and place the logo somewhere on the page...logo attached and images attached -- happy to provide more images if necessary

You can play with images, zoom in, dont need to use whole image, etc....modern, classy, airy.

thanks.

Target Market(s)

35-60 year old women, modern, elegant, look conscious

Number of Pages Required

1 page

Font styles to use
Sans Serif

Requirements
Must have
• Images fade from one to other slowly and elegantly -- or slide, etc..some sort of elegant transition
• Opaque, airy feel
• logo must be present and easy to identify
Should not have
• NO SOUND
• NO SCRIPT TEXT

```html
<!DOCTYPE html>
<html lang="en">
<head>
<meta charset="utf-8">
<title>glowparlorqz.com coming soon</title>
<link rel="stylesheet" href="https://fonts.googleapis.com/css2?family=Raleway:wght@200;300;400&family=Roboto+Condensed:wght@300;400&display=swap">
<style>
  :root {
    --bg-top: #4a5157;
    --bg-bottom: #33393e;
    --bg-warm: #7a675b;
    --bg-soft: rgba(122, 103, 91, 0);
    --veil: rgba(255, 255, 255, 0.06);
    --text: #ffffff;
    --text-soft: rgba(255, 255, 255, 0.92);
    --line: rgba(255, 255, 255, 0.85);
    --social-1: #6f8db8;
    --social-2: #c9626a;
    --social-3: #6fb7da;
    --social-4: #d07a6e;
    --social-5: #e3a65e;
  }
  * { margin: 0; padding: 0; box-sizing: border-box; }
  html, body {
    width: 1200px;
    height: 701px;
    overflow: hidden;
    background: var(--bg-bottom);
  }
  .page {
    position: relative;
    width: 1200px;
    height: 701px;
    overflow: hidden;
    font-family: "Raleway", sans-serif;
    color: var(--text);
  }
  .hero-photo {
    position: absolute;
    inset: 0;
    background:
      radial-gradient(ellipse 320px 400px at 590px 320px, var(--bg-warm) 0%, rgba(122, 103, 91, 0.45) 55%, var(--bg-soft) 100%),
      linear-gradient(180deg, var(--bg-top) 0%, var(--bg-bottom) 100%);
  }
  .hero-veil {
    position: absolute;
    inset: 0;
    background: var(--veil);
  }
  .brand {
    position: absolute;
    top: 166px;
    left: 0;
    width: 100%;
    text-align: center;
    font-weight: 300;
    font-size: 52px;
    letter-spacing: 1px;
    line-height: 1;
  }
  .headline {
    position: absolute;
    top: 236px;
    left: 0;
    width: 100%;
    text-align: center;
    font-weight: 300;
    font-size: 58px;
    line-height: 1;
  }
  .tagline {
    position: absolute;
    top: 309px;
    left: 0;
    width: 100%;
    text-align: center;
    font-weight: 300;
    font-size: 31px;
    line-height: 1;
    color: var(--text-soft);
  }
  .countdown-unit {
    position: absolute;
    top: 376px;
    width: 110px;
    margin-left: -55px;
    text-align: center;
  }
  .countdown-unit svg { display: block; margin: 0 auto; }
  .countdown-value {
    position: absolute;
    top: 51px;
    left: 0;
    width: 100%;
    transform: translateY(-50%);
    font-family: "Roboto Condensed", sans-serif;
    font-weight: 400;
    font-size: 22px;
  }
  .countdown-label {
    margin-top: 20px;
    font-size: 19px;
    font-weight: 400;
  }
  .social-links {
    position: absolute;
    top: 624px;
    left: 0;
    width: 100%;
    display: flex;
    justify-content: center;
    gap: 11px;
  }
  .social-link {
    width: 25px;
    height: 25px;
    border-radius: 2px;
  }
  .social-link.s1 { background: var(--social-1); }
  .social-link.s2 { background: var(--social-2); }
  .social-link.s3 { background: var(--social-3); }
  .social-link.s4 { background: var(--social-4); }
  .social-link.s5 { background: var(--social-5); }
</style>
</head>
<body>
<main class="page">
  <div class="hero-photo" role="img" aria-label="Photograph of a woman with long brown hair tossed upward, wearing a black halter top, softly lit"></div>
  <div class="hero-veil"></div>

  <div class="brand">glowparlorqz</div>
  <h1 class="headline">beauty, simplified.</h1>
  <p class="tagline">it doesn't have to be complicated</p>

  <div class="countdown-unit" style="left:409px">
    <svg width="102" height="102" viewBox="0 0 102 102"><rect x="15.5" y="15.5" width="71" height="71" rx="3" transform="rotate(45 51 51)" fill="none" stroke="var(--line)" stroke-width="1"/></svg>
    <div class="countdown-value">118</div>
    <div class="countdown-label">days</div>
  </div>
  <div class="countdown-unit" style="left:536px">
    <svg width="102" height="102" viewBox="0 0 102 102"><rect x="15.5" y="15.5" width="71" height="71" rx="3" transform="rotate(45 51 51)" fill="none" stroke="var(--line)" stroke-width="1"/></svg>
    <div class="countdown-value">02</div>
    <div class="countdown-label">hours</div>
  </div>
  <div class="countdown-unit" style="left:664px">
    <svg width="102" height="102" viewBox="0 0 102 102"><rect x="15.5" y="15.5" width="71" height="71" rx="3" transform="rotate(45 51 51)" fill="none" stroke="var(--line)" stroke-width="1"/></svg>
    <div class="countdown-value">34</div>
    <div class="countdown-label">minutes</div>
  </div>
  <div class="countdown-unit" style="left:791px">
    <svg width="102" height="102" viewBox="0 0 102 102"><rect x="15.5" y="15.5" width="71" height="71" rx="3" transform="rotate(45 51 51)" fill="none" stroke="var(--line)" stroke-width="1"/></svg>
    <div class="countdown-value">36</div>
    <div class="countdown-label">seconds</div>
  </div>

  <nav class="social-links" aria-label="Social links">
    <span class="social-link s1" aria-label="Social link 1"></span>
    <span class="social-link s2" aria-label="Social link 2"></span>
    <span class="social-link s3" aria-label="Social link 3"></span>
    <span class="social-link s4" aria-label="Social link 4"></span>
    <span class="social-link s5" aria-label="Feed link"></span>
  </nav>
</main>
</body>
</html>
```